Eyewear store

-The design must be based around the attached HPID (home page information design) called Lens at Marlowe HPID. I've attached Word and PDF versions - these are the same. The table boxes are just for approximate placement of information – you DON'T have to box everything in and you can arrange these. All fonts used in the HPID are only examples - you can use any Google font you wish.
- Information only is in orange text. Copy to go on the design in black text. Some instructions are in the HPID. Please be creative!
-The design needs to be modern. Colours are to be brown, green, black and white ...refer to the shop images in the HPID. Keep it clean and simple, don't need to use all the colours.
- I've provided the images for the site but these are just to show style, use any similar images, but they must be free images.
Width of content will be 1100 pixels when implemented as a web page. Header height (without nav bar) 150-160 pixels.
If your design is chosen the winning PSD file will have to be provided as follows…
1. Canvas size of 2000px x 2000px - 72ppi in Adobe Photoshop (CS5 compatible)
2. Width of content section is 1100px wide - centered in the canvas
3. Any button rollovers/hovers in the PSD as hidden layers.
4. All fonts used must be Google fonts (except for the fonts in the header at the top of the page).
5. You will need to supply the chosen home page plus one example page (example page as a style guide for how all other pages will look). Example page is only the header and navigational bar at the top, an empty sector in the middle with a column (180 px wide) which can be left or right aligned which means the main sector is 920 pixels wide, and then the footer at the bottom of the page
Checklist - http://pagecraftlist.example/
Target Market(s)
Fashion Eyewear lovers
Mid age women
Sportspeople
Teenagers who need prescription
Non-glasses wearers - People looking to buy branded sunglasses (fashion conscious people of all ages)
Industry/Entity Type
Store
Look and feel
Each slider illustrates characteristics of the customer's brand and the style your logo design should communicate.

```html
<!DOCTYPE html>
<html lang="en">
<head>
<meta charset="utf-8">
<title>Lens at Marlowe</title>
<link href="https://fonts.googleapis.com/css2?family=Arimo:wght@400;700&family=Crimson+Text:wght@400;600&family=Roboto:wght@400;500&display=swap" rel="stylesheet">
<style>
:root{
  --blue:#2b84b4;
  --green:#5e7a1f;
  --green-dark:#4c6418;
  --ink:#2a2a2a;
  --grey:#6b6b6b;
  --dark:#141414;
  --caption:#333b40;
  --rule:#d8d8d8;
  --white:#ffffff;
}
*{box-sizing:border-box;margin:0;padding:0}
html,body{width:982px;height:1200px;overflow:hidden;background:var(--white)}
body{position:relative;font-family:"Arimo",Arial,sans-serif;color:var(--ink)}
.abs{position:absolute}

.topline{left:0;top:0;width:982px;height:4px;background:#2c2c2c}
.logo{left:76px;top:46px;font-family:"Roboto",sans-serif;font-weight:500;font-size:29px;color:#777;letter-spacing:.5px;display:flex;align-items:center;gap:8px}
.logo .dot{width:14px;height:14px;border-radius:50%;background:var(--blue)}
.tagline{left:440px;top:38px;width:245px;text-align:right;font-family:"Crimson Text",serif;font-weight:600;font-size:15.5px;line-height:20px;color:var(--green)}
.tagline .last{color:var(--blue)}
.vrule{left:700px;top:32px;width:2px;height:70px;background:#e4e4e4}
.call{left:735px;top:24px;font-family:"Roboto",sans-serif;font-size:19px;color:var(--green);display:flex;align-items:center;gap:6px}
.call span{font-size:14px;color:var(--ink);margin-left:8px}
.addr{left:720px;top:53px;font-family:"Crimson Text",serif;font-size:13px;color:#555;display:flex;align-items:center;gap:6px}
.social{left:803px;top:79px;width:107px;height:34px;border:1px solid #ccc;border-radius:3px;background:#f1f1f1;display:flex;align-items:center;gap:6px;padding-left:5px;font-family:"Roboto",sans-serif;font-size:12px;color:var(--blue)}
.social .sq{width:22px;height:22px;background:var(--blue);border-radius:2px}

.nav{left:0;top:121px;width:982px;height:35px;background:var(--blue)}
.nav ul{list-style:none;position:absolute;left:69px;top:0;display:flex;height:35px}
.nav li{font-family:"Roboto",sans-serif;font-size:11.5px;color:var(--white);line-height:35px;padding:0 8.5px;border-right:1px solid rgba(255,255,255,.18)}
.nav li.active{background:var(--green);font-weight:500;padding:0 11px}
.nav li:last-child{border-right:none}

.hero{left:0;top:156px;width:752px;height:344px;background:linear-gradient(90deg,#eceeed 0%,#e3e5e4 45%,#c9cbca 70%,#9ea09f 100%)}
.hero-title{left:70px;top:300px;font-family:"Crimson Text",serif;font-size:31px;color:#8b8f90;letter-spacing:.5px}
.dots{left:82px;top:475px;display:flex;gap:6px}
.dots i{width:10px;height:10px;border-radius:50%;background:var(--green)}
.dots i:first-child{background:var(--blue)}
.side{left:752px;top:156px;width:230px;height:344px;background:#f4f4f4}
.tile{position:absolute;left:759px;width:155px;height:62px;border:3px solid var(--blue);background:#f7f7f7}
.tile .ph{position:absolute;left:0;top:0;width:100%;height:41px;background:linear-gradient(90deg,#f0f0f0,#c8cbcc,#f0f0f0)}
.tile .cap{position:absolute;left:0;bottom:0;width:100%;height:15px;background:var(--caption);color:var(--white);font-size:10.5px;text-align:center;line-height:15px}
.heroline{left:0;top:499px;width:982px;height:3px;background:#2c2c2c}

.card{position:absolute;top:516px;height:316px;border:1px solid var(--rule);background:var(--white);box-shadow:0 1px 3px rgba(0,0,0,.08)}
.card h2{height:43px;background:var(--blue);color:var(--white);font-family:"Crimson Text",serif;font-weight:600;font-size:15.5px;line-height:17px;text-align:center;padding-top:5px}
.card .ph{margin:3px 3px 0;height:118px}
.card p{font-size:10.3px;line-height:14px;padding:7px 7px 0 7px;color:#333}
.btn{position:absolute;left:5px;width:105px;height:29px;background:var(--green);color:var(--white);font-family:"Roboto",sans-serif;font-weight:500;font-size:11.5px;line-height:29px;padding-left:8px;clip-path:polygon(0 0,88% 0,100% 50%,88% 100%,0 100%)}

.brands{left:70px;top:858px;width:845px;height:72px;border:1px solid var(--rule);box-shadow:0 1px 3px rgba(0,0,0,.08);background:var(--white)}
.brands-label{left:78px;top:882px;width:105px;height:30px;background:var(--green);color:var(--white);font-family:"Crimson Text",serif;font-size:18px;line-height:30px;padding-left:5px;clip-path:polygon(0 0,90% 0,100% 50%,90% 100%,0 100%)}
.brand-row{left:205px;top:882px;width:705px;height:30px;display:flex;justify-content:space-between;align-items:center}
.brand-row span{font-family:"Crimson Text",serif;font-weight:600;font-size:17px;color:#8a8a8a}

.footer{left:0;top:962px;width:982px;height:210px;background:var(--dark)}
.fhead{font-family:"Crimson Text",serif;font-size:14.5px;color:var(--white);padding-bottom:3px;border-bottom:1px dashed #555}
.qlinks{left:70px;top:973px;width:132px}
.qlinks ul{list-style:none;margin-top:7px}
.qlinks li{font-size:10px;color:var(--white);line-height:17px;padding-left:16px;position:relative}
.qlinks li::before{content:"›";position:absolute;left:3px;top:-1px;color:#ccc}
.hours{left:252px;top:975px;width:168px}
.hours table{margin-top:7px;border-collapse:collapse}
.hours td{font-size:10px;color:var(--white);line-height:20px;padding-right:18px}
.fhead2{font-family:"Arimo",sans-serif;font-size:13.5px;color:var(--white);padding-bottom:3px;border-bottom:1px dashed #555}
.address{left:252px;top:1081px;width:168px}
.address p{font-size:10px;color:var(--white);line-height:14.5px;margin:7px 0 0 17px;position:relative}
.address svg{position:absolute;left:-17px;top:2px}
.fdivide{top:975px;width:1px;height:190px;background:#262626}
.stores{left:468px;top:975px;width:208px}
.store-panel{left:468px;top:1005px;width:208px;height:159px;background:#a9a9a9}
.store-a{left:473px;top:1012px;width:194px;height:29px;background:#1d2569;color:var(--white);font-family:"Arimo",sans-serif;font-weight:700;font-size:13px;line-height:29px;padding-left:5px}
.viewlink{font-size:12px;color:#333;text-decoration:underline}
.store-b{left:477px;top:1100px;width:165px;font-family:"Roboto",sans-serif;font-weight:500;font-size:12.5px;color:#222;border-bottom:1px solid var(--blue);padding-bottom:2px;display:flex;align-items:center;justify-content:space-between}
.store-b i{width:14px;height:14px;background:var(--blue)}
.flogo{left:720px;top:1020px;font-family:"Roboto",sans-serif;font-weight:500;font-size:22px;color:#ccc;display:flex;align-items:center;gap:7px}
.flogo .dot{width:12px;height:12px;border-radius:50%;background:#ccc}
.fsocial{left:743px;top:1098px;width:139px;height:46px;background:var(--white);border:1px solid #ccc;display:flex;align-items:center;gap:8px;padding-left:6px;font-family:"Roboto",sans-serif;font-size:15px;color:var(--blue)}
.fsocial .sq{width:32px;height:32px;background:var(--blue);border-radius:3px}
.bottom{left:0;top:1172px;width:982px;height:28px;background:var(--blue);color:var(--white);font-size:10px;text-align:center;line-height:28px}
</style>
</head>
<body>
<div class="abs topline"></div>

<header>
  <div class="abs logo"><i class="dot"></i>LENS AT MARLOWE</div>
  <div class="abs tagline">For Stylish Sunglasses,<br>Prescription Glasses &amp; Eye Exams<br><span class="last">In Kereru Bay</span></div>
  <div class="abs vrule"></div>
  <div class="abs call">
    <svg width="14" height="18" viewBox="0 0 14 18"><path d="M3 1l3 1-1 4-2 1c1 3 3 6 5 8l2-1 3 2-1 3c-6-1-11-9-11-15z" fill="#5e7a1f"/></svg>
    Call Us <span>(06) 555 0148</span>
  </div>
  <div class="abs addr">
    <svg width="10" height="14" viewBox="0 0 10 14"><path d="M5 0a5 5 0 0 0-5 5c0 4 5 9 5 9s5-5 5-9a5 5 0 0 0-5-5zm0 7a2 2 0 1 1 0-4 2 2 0 0 1 0 4z" fill="#5e7a1f"/></svg>
    97A Marlowe Avenue, Kereru Bay
  </div>
  <div class="abs social"><i class="sq"></i>Social Page</div>
</header>

<nav class="abs nav">
  <ul>
    <li class="active">HOME</li><li>ABOUT</li><li>EYEWEAR</li><li>BOOK AN EYE EXAM</li><li>SPECIALS / PROMOTIONS</li><li>ALL ABOUT EYES</li><li>NEWS</li><li>ARTICLES</li><li>OTHER STORES</li><li>CONTACT</li>
  </ul>
</nav>

<section class="abs hero" role="img" aria-label="Black and white photo of a woman wearing dark sunglasses, on the right"></section>
<div class="abs hero-title">THREE STORES, ONE VISION</div>
<div class="abs dots"><i></i><i></i><i></i><i></i></div>

<aside class="abs side"></aside>
<div class="tile" style="top:159px"><div class="ph" role="img" aria-label="Eye test letter chart"></div><div class="cap">Book an Eye Exam</div></div>
<div class="tile" style="top:227px"><div class="ph" role="img" aria-label="Close up of blue eyes"></div><div class="cap">All About Eyes</div></div>
<div class="tile" style="top:294px"><div class="ph" role="img" aria-label="New glasses in store"></div><div class="cap">What's New In Store</div></div>
<div class="tile" style="top:365px"><div class="ph" role="img" aria-label="Pair of eyeglass frames"></div><div class="cap">Eyewear</div></div>
<div class="tile" style="top:436px"><div class="ph" role="img" aria-label="Woman in stylish glasses"></div><div class="cap">Promotions &amp; Specials</div></div>
<div class="abs heroline"></div>

<article class="card" style="left:70px;width:274px">
  <h2>Largest Sunglasses Selection<br>In Kereru Bay</h2>
  <div class="ph" role="img" aria-label="Woman in mirrored sunglasses sitting on sand" style="background:linear-gradient(90deg,#d9c3a6,#b89a7c,#e2d2bc)"></div>
  <p>For the latest brands and designer sunglasses come in and see the friendly team at Lens at Marlowe. There's something for everyone with thousands of glasses in store – view our selection online now.</p>
  <p style="padding-top:5px">We're also the exclusive stockist in Kereru Bay of Solvane sunglasses and optical frames.</p>
  <div class="btn" style="top:280px">Find Out More</div>
</article>

<article class="card" style="left:355px;width:274px">
  <h2>Kereru Bay's Prescription Glasses<br>Experts Perfect Fit Guaranteed</h2>
  <div class="ph" role="img" aria-label="Woman in glasses reading a tablet beside a bookshelf" style="background:linear-gradient(90deg,#e8b46a,#d98a3a,#efe9e2)"></div>
  <p>Lens at Marlowe is your One-Stop-Shop Eyecare store and have a huge range of prescription lenses, contact lenses and the very latest European trend-setting fashion eye-wear.</p>
  <p style="padding-top:5px">Take a look at our selection of prescription glasses now.</p>
  <div class="btn" style="top:275px">Find Out More</div>
</article>

<article class="card" style="left:639px;width:275px">
  <h2>For Eye Exams In The Heart Of<br>Kereru Bay</h2>
  <div class="ph" role="img" aria-label="Black glasses resting on an eye chart" style="background:linear-gradient(90deg,#e6e6e6,#bdbdbd,#e9e9e9)"></div>
  <p>Lens at Marlowe offers complete eye examinations in store. Our Optometrists offer free annual check-ups and glasses fitting.</p>
  <p style="padding-top:5px">And all our glasses come with a full replacement warranty on all new frames and lenses sold – Book an appointment now</p>
  <div class="btn" style="top:280px">Find Out More</div>
</article>

<section class="abs brands"></section>
<div class="abs brands-label">Our Brands</div>
<div class="abs brand-row">
  <span>ARDENT</span><span>Vela Moda</span><span>Tide Line</span><span>Solvane</span><span>CORBETTI</span><span>Lumière</span><span>OSTRA</span>
</div>

<footer>
  <div class="abs footer"></div>
  <div class="abs qlinks">
    <div class="fhead">Quick Links</div>
    <ul><li>Home</li><li>About</li><li>Eyewear</li><li>Book an Eye Exam</li><li>Specials/Promotions</li><li>News</li><li>Articles</li><li>Other Stores</li><li>Contact</li></ul>
  </div>
  <div class="abs fdivide" style="left:232px"></div>
  <div class="abs hours">
    <div class="fhead">Open Hours</div>
    <table>
      <tr><td>Monday - Friday</td><td>9am - 5pm</td></tr>
      <tr><td>Saturday</td><td>9am - 1pm</td></tr>
      <tr><td>Statutory Holidays</td><td>closed</td></tr>
    </table>
  </div>
  <div class="abs address">
    <div class="fhead2">Address</div>
    <p><svg width="10" height="14" viewBox="0 0 10 14"><path d="M5 0a5 5 0 0 0-5 5c0 4 5 9 5 9s5-5 5-9a5 5 0 0 0-5-5zm0 7a2 2 0 1 1 0-4 2 2 0 0 1 0 4z" fill="#fff"/></svg>97A Marlowe Avenue<br>Kereru Bay 4599<br>New Zealand</p>
  </div>
  <div class="abs fdivide" style="left:445px"></div>
  <div class="abs stores"><div class="fhead">Other Stores</div></div>
  <div class="abs store-panel"></div>
  <div class="abs store-a">Harbour Eyecare Centre</div>
  <div class="abs viewlink" style="left:474px;top:1047px">View website</div>
  <div class="abs store-b">Tarnby Eyecare<i></i></div>
  <div class="abs viewlink" style="left:475px;top:1130px">View website</div>
  <div class="abs flogo"><i class="dot"></i>LENS AT MARLOWE</div>
  <div class="abs fsocial"><i class="sq"></i>Social Page</div>
  <div class="abs bottom">© 2015 LENSATMARLOWE. All Rights Reserved.</div>
</footer>
</body>
</html>
```